Business Card Design

I need a business card for my resume writing business. I have a logo that Im not keen on anymore so I would like the business card to use my photo instead of a logo. I am for mid career and trades resumes and prefer not to do executive resumes so don't need to aim for exectives. I would like it to be colourful. I like bright sky blue and maybe some pink or purple but primarily bright sky blue. I don't like green and Im keen see a fair bit of white on the card. As I have a photo to go it, it will need to go on a white background.

Target Market(s)

mid range careers. Not executives

Industry/Entity Type

Business

Contact Information for Business Card

Lise Varncombe
Resume Writer
Bright Path CVs
27 The Gullwing
HALDORN NSW 2391
lise@brightpathcvs.com.au
0417263958
www.brightpathcvs.com.au

Requirements
Nice to have
• Maybe colours similar to my website - www.brightpathcvs.com.au but not with any black on it.
Should not have
• No green or dark colours

```html
<!DOCTYPE html>
<html lang="en">
<head>
<meta charset="utf-8">
<title>Lise Varncombe – Business Card</title>
<link rel="stylesheet" href="https://fonts.googleapis.com/css2?family=Arimo:ital,wght@0,400;0,700;1,400&family=Michroma&display=swap">
<style>
  :root {
    --page-bg: #eef0f2;
    --card-light: #f4fbff;
    --card-sky: #b9e6f8;
    --panel-blue-deep: #0a55b0;
    --panel-blue-bright: #1d8de0;
    --slate: #3b4b5e;
    --accent-orange: #f05a2c;
    --name-navy: #1e2f8c;
    --ink: #1b1b1b;
    --white: #ffffff;
  }
  * { margin: 0; padding: 0; box-sizing: border-box; }
  html, body {
    width: 968px;
    height: 1200px;
    overflow: hidden;
    background: var(--page-bg);
  }
  .business-card {
    position: absolute;
    left: 44px;
    top: 330px;
    width: 880px;
    height: 541px;
    overflow: hidden;
    background: linear-gradient(120deg, var(--card-light) 0%, #dff3fc 45%, var(--card-sky) 100%);
    box-shadow: 0 2px 6px rgba(0,0,0,0.25);
    font-family: "Arimo", Arial, sans-serif;
  }
  .card-shapes {
    position: absolute;
    inset: 0;
  }
  .contact-line {
    position: absolute;
    left: 164px;
    color: var(--white);
    font-size: 22px;
    line-height: 1;
    white-space: nowrap;
  }
  .contact-address-1 { top: 113px; }
  .contact-address-2 { top: 141px; }
  .contact-phone { top: 183px; }
  .contact-email { top: 253px; }
  .website {
    position: absolute;
    left: 62px;
    top: 412px;
    color: var(--white);
    font-size: 22px;
    letter-spacing: 0.3px;
  }
  .portrait {
    position: absolute;
    left: 594px;
    top: 72px;
    width: 210px;
    height: 205px;
    border: 3px solid var(--slate);
    border-radius: 16px;
    background: radial-gradient(circle at 50% 40%, #8a5a44 0%, #c9a08a 30%, #eaeaea 62%, #f6f6f6 100%);
  }
  .holder-name {
    position: absolute;
    left: 594px;
    width: 210px;
    top: 289px;
    text-align: center;
    font-family: "Michroma", "Arimo", sans-serif;
    font-weight: 400;
    font-size: 19px;
    color: var(--name-navy);
    white-space: nowrap;
    letter-spacing: 0.5px;
    -webkit-text-stroke: 0.6px var(--name-navy);
  }
  .holder-role {
    position: absolute;
    left: 594px;
    width: 210px;
    top: 318px;
    text-align: center;
    font-style: italic;
    font-size: 18px;
    color: var(--ink);
  }
</style>
</head>
<body>
  <section class="business-card" aria-label="Business card for Lise Varncombe, Bright Path CVs">
    <svg class="card-shapes" width="880" height="541" viewBox="0 0 880 541" aria-hidden="true">
      <defs>
        <radialGradient id="panelGlow" cx="0.15" cy="0.1" r="1">
          <stop offset="0" stop-color="var(--panel-blue-bright)"/>
          <stop offset="1" stop-color="var(--panel-blue-deep)"/>
        </radialGradient>
        <linearGradient id="urlBand" x1="0" y1="0" x2="1" y2="0">
          <stop offset="0" stop-color="#0b5fbf"/>
          <stop offset="1" stop-color="#0a4f9e"/>
        </linearGradient>
      </defs>

      <!-- contact panel with chevron edge -->
      <polygon class="contact-panel" points="37,37 463,37 507,199 463,360 37,360" fill="url(#panelGlow)"/>
      <!-- slate chevron stripe -->
      <polygon class="chevron-stripe" points="476,37 494,37 538,199 494,360 476,360 520,199" fill="var(--slate)"/>

      <!-- icon pills -->
      <g class="icon-pill" fill="var(--slate)" stroke="var(--white)" stroke-width="3">
        <path d="M30,106 H127 a23,23 0 0 1 0,46 H30 Z"/>
        <path d="M30,176 H127 a23,23 0 0 1 0,46 H30 Z"/>
        <path d="M30,247 H127 a23,23 0 0 1 0,46 H30 Z"/>
      </g>
      <!-- home icon -->
      <g class="icon-home" fill="var(--white)">
        <polygon points="101,116 86,129 90,129 90,142 98,142 98,134 104,134 104,142 112,142 112,129 116,129"/>
      </g>
      <!-- phone icon -->
      <g class="icon-phone" fill="none" stroke="var(--white)" stroke-width="2">
        <circle cx="101" cy="199" r="13"/>
        <path d="M95,192 q-2,4 2,10 q4,6 9,5 l2,-3 l-4,-3 l-2,2 q-3,-2 -4,-6 l2,-1 l-2,-4 Z" fill="var(--white)" stroke="none"/>
      </g>
      <!-- envelope icon -->
      <g class="icon-mail">
        <rect x="88" y="261" width="28" height="19" fill="var(--white)"/>
        <polyline points="88,261 102,272 116,261" fill="none" stroke="var(--slate)" stroke-width="1.5"/>
      </g>

      <!-- website band -->
      <polygon class="website-band" points="37,400 482,400 496,448 37,448" fill="url(#urlBand)"/>
      <!-- orange accent band -->
      <polygon class="accent-band" points="502,450 845,450 845,502 524,502" fill="var(--accent-orange)"/>
    </svg>

    <p class="contact-line contact-address-1">27 The Gullwing HALDORN</p>
    <p class="contact-line contact-address-2">NSW 2391</p>
    <p class="contact-line contact-phone">0417263958</p>
    <p class="contact-line contact-email">lise@brightpathcvs.com.au</p>

    <p class="website">www.brightpathcvs.com.au</p>

    <div class="portrait" role="img" aria-label="Portrait photograph of Lise Varncombe"></div>
    <p class="holder-name">LISE VARNCOMBE</p>
    <p class="holder-role">Writer</p>
  </section>
</body>
</html>
```